Apricot Variety Sheet - Meadowlark Orchard Co

We are needing a variety sheet that we can hand out that will describe the different apricot vatieties we have available. The attached document has the name of the variety along with a description that will need to be on the sheet. We are looking for a modern, appealing way to display this information on 1 page (if needed, it can be front and back)
Updates

Apologies for the delay; we are overwhelmed with the great design options and will be sorting through them all (across our contests) to pick a collective. Thank you for your patience.

Target Market(s)

Growers and consumers

Industry/Entity Type

Agriculture

Requirements
Must have
• Easy to read
• Natural color palettes to emphasize the agricultural nature
• Clearly show washington as the origin in the title or at the top
Nice to have
• incorporate Apricots in the design

```html
<!DOCTYPE html>
<html lang="en">
<head>
<meta charset="utf-8">
<title>Apricot Variety Sheet – Meadowlark Orchard Co</title>
<link href="https://fonts.googleapis.com/css2?family=Lobster&family=Karla:ital,wght@0,400;0,700;1,700&family=Nunito:wght@800&display=swap" rel="stylesheet">
<style>
  :root {
    --wood-light: #f1f1f0;
    --wood-mid: #dcdcda;
    --frame: #ffffff;
    --ink: #2b2b2b;
    --title-ink: #333333;
    --plum: #8a3a4e;
    --rule: #9b5566;
    --apricot: #f39a3a;
    --apricot-deep: #e2752a;
    --apricot-light: #fbc06a;
    --teal: #5bbfb2;
    --plate: #f6f7fb;
    --green: #1f7a3e;
  }
  * { box-sizing: border-box; margin: 0; padding: 0; }
  html, body { width: 849px; height: 1200px; overflow: hidden; }
  body {
    position: relative;
    font-family: "Karla", sans-serif;
    color: var(--ink);
    background: linear-gradient(180deg, var(--wood-light) 0%, var(--wood-mid) 50%, var(--wood-light) 100%);
  }
  .sheet-frame {
    position: absolute; left: 50px; top: 48px; width: 750px; height: 1104px;
    border: 3px solid var(--frame);
  }
  .photo { position: absolute; }
  .photo-bowl-top {
    left: -40px; top: -50px; width: 250px; height: 240px; border-radius: 50%;
    background: radial-gradient(circle at 55% 55%, var(--apricot) 0 45%, var(--apricot-deep) 55%, var(--teal) 62%, #3f9d91 70%);
  }
  .photo-halves-top {
    left: 40px; top: 150px; width: 150px; height: 80px; border-radius: 50%;
    background: radial-gradient(ellipse at 60% 45%, var(--apricot-light), var(--apricot-deep));
  }
  .photo-plate {
    left: 640px; top: -40px; width: 240px; height: 230px; border-radius: 50%;
    background: radial-gradient(circle at 45% 45%, var(--apricot) 0 28%, var(--plate) 34%, #e4e6ee 100%);
  }
  .photo-colander {
    left: 642px; top: 672px; width: 260px; height: 360px; border-radius: 50%;
    background: radial-gradient(circle at 45% 50%, var(--apricot) 0 40%, var(--apricot-deep) 55%, #f3ecde 62%, #c9bfa8 70%);
  }
  .photo-bowl-bottom {
    left: -30px; top: 940px; width: 222px; height: 280px; border-radius: 50%;
    background: radial-gradient(circle at 50% 50%, var(--apricot-light) 0 35%, var(--apricot) 55%, #eef0ec 62%, #cfd6cf 70%);
  }
  .photo-apricot-single {
    left: 662px; top: 1034px; width: 96px; height: 96px; border-radius: 50%;
    background: radial-gradient(circle at 40% 40%, var(--apricot-light), var(--apricot));
  }
  .photo-knife {
    left: 490px; top: 1120px; width: 359px; height: 80px;
    background: linear-gradient(172deg, transparent 40%, #b8bcc2 41% 55%, #222 56% 68%, transparent 69%);
  }
  .title-block { position: absolute; left: 0; width: 849px; top: 46px; text-align: center; }
  .title-origin {
    font-weight: 700; font-size: 13px; letter-spacing: 4px; text-transform: uppercase;
    color: var(--plum);
  }
  .title-main {
    font-family: "Lobster", cursive; font-size: 110px; line-height: 1;
    color: var(--title-ink); letter-spacing: 1px;
  }
  .title-sub {
    font-family: "Lobster", cursive; font-size: 34px; color: var(--title-ink);
    margin-top: -6px; margin-left: 20px;
  }
  .variety { position: absolute; width: 156px; }
  .variety-name {
    font-family: "Lobster", cursive; font-size: 26px; line-height: 1; color: var(--ink);
    height: 32px;
  }
  .variety-desc { font-size: 11.4px; line-height: 15px; margin-top: 2px; }
  .variety-avail {
    position: absolute; left: 0; width: 156px;
    border-top: 1px solid var(--rule); border-bottom: 1px solid var(--rule);
    color: var(--plum); font-weight: 700; font-style: italic; font-size: 12.2px; line-height: 15.2px;
    padding-top: 7px;
  }
  .row-1 .variety-avail { top: 143px; height: 44px; }
  .row-2 .variety-avail { top: 128px; height: 44px; }
  .row-3 .variety-avail { top: 114px; height: 44px; }
  .featured { position: absolute; left: 232px; top: 904px; width: 410px; }
  .featured .variety-name { font-size: 32px; height: 38px; }
  .featured .variety-desc { font-size: 12.4px; line-height: 16px; }
  .featured-avail {
    position: absolute; left: 172px; top: 988px; width: 314px; height: 34px;
    background: var(--apricot); color: var(--ink);
    font-weight: 700; font-size: 13px; line-height: 34px; padding-left: 60px;
  }
  .maker { position: absolute; left: 232px; top: 1040px; display: flex; align-items: center; gap: 22px; }
  .maker-mark { width: 96px; height: 96px; border-radius: 50%; background: var(--apricot-deep); }
  .maker-name {
    font-family: "Nunito", sans-serif; font-weight: 800; font-size: 27px; line-height: 28px;
    color: var(--green); width: 260px;
  }
</style>
</head>
<body>
  <div class="sheet-frame"></div>

  <div class="photo photo-bowl-top" role="img" aria-label="Teal bowl of whole apricots"></div>
  <div class="photo photo-halves-top" role="img" aria-label="Apricot halves and slices"></div>
  <div class="photo photo-plate" role="img" aria-label="White plate with halved apricots"></div>
  <div class="photo photo-colander" role="img" aria-label="Colander filled with ripe apricots"></div>
  <div class="photo photo-bowl-bottom" role="img" aria-label="Bowl of sliced apricots with thyme"></div>
  <div class="photo photo-apricot-single" role="img" aria-label="Single whole apricot"></div>
  <div class="photo photo-knife" role="img" aria-label="Kitchen knife on the table"></div>

  <header class="title-block">
    <p class="title-origin">Washington Grown</p>
    <h1 class="title-main">Apricot</h1>
    <p class="title-sub">Variety Sheet</p>
  </header>

  <section class="row-1">
    <article class="variety" style="left:70px;top:264px">
      <h2 class="variety-name">Rival</h2>
      <p class="variety-desc">Great flavor with a fine, firm texture distinguishes this large oval-shaped apricot. The skin is light orange with a red blush. The flesh is a lush deep orange color.</p>
      <p class="variety-avail">Available early<br>July- early August.</p>
    </article>
    <article class="variety" style="left:254px;top:264px">
      <h2 class="variety-name">Robada</h2>
      <p class="variety-desc">This jumbo apricot has a delicious floral flavor with a firm texture. Bright orange, with a deep red blush over nearly half its surface.</p>
      <p class="variety-avail">Available early June.</p>
    </article>
    <article class="variety" style="left:438px;top:264px">
      <h2 class="variety-name">Perfection</h2>
      <p class="variety-desc">This classic large oval apricot is deep orange with an oblong shape and firm texture. The flesh is a yellow/orange color that is very sweet and full of flavor.</p>
      <p class="variety-avail">Available<br>mid July - mid August.</p>
    </article>
    <article class="variety" style="left:622px;top:264px">
      <h2 class="variety-name">Patterson</h2>
      <p class="variety-desc">This apricot has a well-balanced flavor and an excellent shelf life. This is perfect for canning or drying. It has streaked red over yellow skin, with a firm flesh.</p>
      <p class="variety-avail">Available mid – late June.</p>
    </article>
  </section>

  <section class="row-2">
    <article class="variety" style="left:70px;top:494px">
      <h2 class="variety-name">Tomcot</h2>
      <p class="variety-desc">Tangy, sweet flavor with a firm texture. This oval apricot is light orange with a slight blush color. The flesh is a dark orange.</p>
      <p class="variety-avail">Available<br>late June – late July.</p>
    </article>
    <article class="variety" style="left:254px;top:494px">
      <h2 class="variety-name">Goldrich</h2>
      <p class="variety-desc">This apricot is round with a bright orange skin color and a deep orange flesh. It has a mild, sweet flavor with a firm texture.</p>
      <p class="variety-avail">Available<br>early July – mid August.</p>
    </article>
    <article class="variety" style="left:438px;top:494px">
      <h2 class="variety-name">Casselbrite</h2>
      <p class="variety-desc">This medium sized apricot is golden orange with a slight red blush. It has a mild sweet-tart flavor that is good for eating out of hand.</p>
      <p class="variety-avail">Available<br>late June- early July.</p>
    </article>
    <article class="variety" style="left:622px;top:494px">
      <h2 class="variety-name">Goldbar</h2>
      <p class="variety-desc">Moderately juicy, this large oval-shaped apricot has a light yellow-orange with a reddish blush. The flesh is firm, meaty, and has a light orange color.</p>
      <p class="variety-avail">Available<br>late June – end of July.</p>
    </article>
  </section>

  <section class="row-3">
    <article class="variety" style="left:70px;top:706px">
      <h2 class="variety-name">Sweet Juille</h2>
      <p class="variety-desc">This special variety has a unique, sweet flavor with a juicy flesh. It is bright orange in color with a bright orange flesh.</p>
      <p class="variety-avail">Available<br>through July.</p>
    </article>
    <article class="variety" style="left:254px;top:706px">
      <h2 class="variety-name">Tasty Rich</h2>
      <p class="variety-desc">This early variety is light yellow-orange colored with a firm texture. Very juicy with an enticing flavor.</p>
      <p class="variety-avail">Available<br>through June.</p>
    </article>
    <article class="variety" style="left:438px;top:706px">
      <h2 class="variety-name">Goldstrike</h2>
      <p class="variety-desc">A larger apricot with light orange, blushed skin. Firm texture with a slight tart taste until fully ripened, then very sweet.</p>
      <p class="variety-avail">Available<br>mid June - mid July.</p>
    </article>
  </section>

  <article class="featured">
    <h2 class="variety-name">Riland</h2>
    <p class="variety-desc">Very aromatic and sweet, this apricot is orange with a red blush. It has a yellow-orange colored flesh and a round shape.</p>
  </article>
  <p class="featured-avail">Available mid-June to end of July.</p>

  <footer class="maker">
    <span class="maker-mark"></span>
    <p class="maker-name">Meadowlark<br>Orchard Co</p>
  </footer>
</body>
</html>
```